依頼詳細
以前こちらで作成して頂いた雰囲気の内容でお願いします。
※添付チラシ

記載項目
・もえぎうたのロゴマークを入れてください。
https://moegiuta.or.jp/event-t/2020-03-14-2 このアドレス用のQRコードを記載してください。
・添付しました画像を使用してください。
サイズ
A4
ページ数
片面
希望イメージ
シンプル 複雑
単色 カラフル
暗い 明るい
日常 高級
遊び心 厳粛
未来的 伝統的
女性的 男性的
希望する色
納品ファイル
補足説明
■ 選んだ理由

ご提案いただきありがとうございました。
どれも良いご提案で悩みましたが、色合いや、雰囲気、読みやすさ、
これから家づくりを考える対象年齢層などを考慮して
選択させて頂きました。

■ 提案者全員のお礼・コメント

多くのご提案を頂きありがとうございました。<m(__)m>

```html
<!DOCTYPE html>
<html lang="ja">
<head>
<meta charset="utf-8">
<title>「家づくり」はじめの一歩 セミナー</title>
<link href="https://fonts.googleapis.com/css2?family=Noto+Sans+JP:wght@400;500;700;900&family=M+PLUS+Rounded+1c:wght@700;800&display=swap" rel="stylesheet">
<style>
:root{
  --green:#8cc63f;
  --green-dark:#5e9b2a;
  --green-pale:#eef6e2;
  --orange:#ee7d22;
  --red:#e8492b;
  --pink:#ef6f8f;
  --ink:#3a2b22;
  --grey:#666;
  --cream:#fbf8f2;
}
*{margin:0;padding:0;box-sizing:border-box}
html,body{width:848px;height:1200px;overflow:hidden;background:#fff}
body{font-family:"Noto Sans JP",sans-serif;color:var(--ink);position:relative}
.flyer{position:absolute;inset:0;background:#fff}
.org-mark{position:absolute;left:34px;top:12px;width:70px;display:flex;flex-direction:column;align-items:center;gap:3px}
.org-mark .dot{width:46px;height:46px;border-radius:50%;background:var(--green-pale);border:3px solid var(--green)}
.org-mark .name{font-size:12px;font-weight:700;color:var(--green-dark);line-height:1.2;white-space:nowrap}
.series{position:absolute;top:26px;left:0;right:0;text-align:center;font-size:26px;font-weight:900;color:var(--green-dark);letter-spacing:2px}
.title{position:absolute;top:78px;left:110px;right:20px;text-align:center;font-family:"M PLUS Rounded 1c",sans-serif;font-weight:800;font-size:54px;line-height:1.2;letter-spacing:1px;color:var(--ink);white-space:nowrap}
.subtitle{position:absolute;top:152px;left:0;right:0;text-align:center;font-size:26px;font-weight:700;color:var(--green-dark);letter-spacing:2px}
.photo-family{position:absolute;left:0;top:200px;width:470px;height:420px;background:linear-gradient(160deg,#f3efe8 0%,#e9dccb 55%,#d8c2a6 100%)}
.photo-house{position:absolute;left:470px;top:330px;width:378px;height:170px;background:linear-gradient(180deg,#f4f2ee,#ddd6cc)}
.points{position:absolute;left:490px;top:205px;width:340px;list-style:none;font-size:16px;font-weight:700;line-height:1.7}
.points li::before{content:"・";color:var(--green-dark)}
.points-note{position:absolute;left:490px;top:290px;width:340px;font-size:11px;line-height:1.6;color:var(--grey)}
.badge{position:absolute;border-radius:50%;color:#fff;display:flex;flex-direction:column;align-items:center;justify-content:center;font-weight:900;text-align:center;line-height:1.2}
.badge.free{left:340px;top:500px;width:104px;height:104px;background:var(--orange);font-size:15px}
.badge.free b{font-size:28px}
.badge.kids{left:416px;top:414px;width:104px;height:104px;background:var(--pink);font-size:13px}
.badge.kids b{font-size:26px;line-height:1.1}
.date{position:absolute;left:36px;top:630px;color:var(--red);font-weight:900;font-size:34px;letter-spacing:1px}
.date .big{font-size:82px;line-height:1}
.date .dow{font-size:40px}
.time{position:absolute;left:70px;top:728px;font-size:18px;font-weight:700}
.venue{position:absolute;left:30px;top:762px;width:440px;display:flex;align-items:center;gap:10px}
.venue .label{background:var(--green);color:#fff;font-weight:700;font-size:14px;width:38px;height:38px;border-radius:50%;display:flex;align-items:center;justify-content:center}
.venue .place{font-size:30px;font-weight:900}
.venue .cap{border:2px solid var(--ink);padding:2px 8px;font-size:15px;font-weight:700}
.address{position:absolute;left:78px;top:806px;font-size:11px;line-height:1.6;color:var(--grey)}
.apply{position:absolute;left:30px;top:862px;display:flex;align-items:center;gap:10px;font-size:17px;font-weight:700}
.apply .tag{background:var(--green-dark);color:#fff;font-size:13px;padding:3px 8px}
.lecturer{position:absolute;left:490px;top:518px;width:340px}
.lecturer .head{font-size:20px;font-weight:900}
.lecturer .head small{font-size:14px;margin-right:6px}
.lecturer p{font-size:11px;line-height:1.6;color:var(--grey);margin-top:6px}
.program{position:absolute;left:490px;top:640px;width:330px;border:2px solid var(--green);border-radius:6px;padding:28px 16px 12px;background:#fff}
.program .lead{position:absolute;top:-14px;left:14px;right:14px;background:#fff;text-align:center;font-size:14px;font-weight:700;color:var(--green-dark)}
.program .tag{display:inline-block;background:var(--green);color:#fff;font-size:13px;font-weight:700;padding:3px 12px;border-radius:12px;margin-bottom:8px}
.program ul{list-style:none;font-size:14px;font-weight:700;line-height:1.75}
.program li::before{content:"●";color:var(--green);margin-right:4px;font-size:11px}
.bottom{position:absolute;left:0;right:0;top:912px;height:270px;background:var(--cream);border-top:3px solid var(--green)}
.office{position:absolute;left:30px;top:930px;font-size:17px;font-weight:700}
.tel{position:absolute;left:30px;top:962px;display:flex;align-items:center;gap:8px}
.tel .num{font-size:58px;font-weight:900;letter-spacing:1px;color:var(--ink);line-height:1}
.fax{position:absolute;left:30px;top:1036px;font-size:15px;font-weight:700;display:flex;gap:16px;align-items:baseline}
.fax span{font-weight:400;font-size:12px;color:var(--grey)}
.web{position:absolute;left:30px;top:1076px;display:flex;align-items:center;gap:12px}
.web .tag{background:var(--green-dark);color:#fff;font-weight:900;font-size:20px;padding:4px 12px}
.web .url{font-size:20px;font-weight:700}
.about{position:absolute;left:520px;top:930px;width:300px;border:2px solid var(--green);background:#fff}
.about h3{background:var(--green);color:#fff;font-size:14px;text-align:center;padding:4px}
.about p{font-size:11px;line-height:1.6;color:var(--grey);padding:8px 10px}
.search{position:absolute;left:520px;top:1100px;width:300px;height:38px;display:flex;border:2px solid var(--green-dark)}
.search .q{flex:1;font-size:16px;font-weight:700;display:flex;align-items:center;padding-left:12px}
.search .btn{width:74px;background:var(--green-dark);color:#fff;font-weight:700;display:flex;align-items:center;justify-content:center;font-size:15px}
.footer-band{position:absolute;left:0;right:0;bottom:0;height:18px;background:var(--green)}
</style>
</head>
<body>
<main class="flyer">
  <div class="org-mark"><span class="dot"></span><span class="name">もえぎうた</span></div>
  <p class="series">暮らしの「学び場」セミナー</p>
  <h1 class="title">「家づくり」はじめの一歩</h1>
  <p class="subtitle">〜後悔しないために学ぶ2つの準備〜</p>

  <div class="photo-family" role="img" aria-label="赤ちゃんと本を読む若い家族の写真"></div>
  <ul class="points">
    <li>夫婦（家族）で決断しておくべきことがある</li>
    <li>計画を進める順番がある</li>
    <li>判断基準を持っておく必要がある</li>
  </ul>
  <p class="points-note">それを知っておくだけで、家づくりの失敗を防ぎ、資金の不安も減り、今後に控える流れもスムーズに進めることができます。</p>
  <div class="photo-house" role="img" aria-label="設計図の上に置かれた白い家の模型の写真"></div>

  <div class="badge kids"><span>子ども連れの</span><span>参加も</span><b>OK</b></div>
  <div class="badge free">参加費<b>無料</b></div>

  <p class="date">2020年<span class="big">3</span>月<span class="big">14</span>日<span class="dow">(土)</span></p>
  <p class="time">13:30〜15:00（受付 13:00〜）</p>
  <div class="venue"><span class="label">会場</span><span class="place">緑風の家</span><span class="cap">定員 先着10名</span></div>
  <p class="address">金沢市青葉町1丁目2番地<br>※お車でお越しの方は、駐車場をご利用ください。<br>主催 一般社団法人 暮らし創造支援機構 もえぎうた</p>
  <p class="apply"><span class="tag">参加申込</span>電話、ホームページにてお申し込みください。</p>

  <section class="lecturer">
    <p class="head"><small>講師</small>もえぎうた認定講師</p>
    <p>家づくりを始める前に知っておくべきことと、知っているとお得なことを、わかりやすく解説します。「家づくり」はじめの一歩をここから始めましょう。</p>
  </section>
  <section class="program">
    <p class="lead">当会認定講師がわかりやすく説明します。</p>
    <span class="tag">セミナー内容</span>
    <ul>
      <li>暮らすイメージをまとめる方法</li>
      <li>住宅購入を決める3つの要因</li>
      <li>土地を買う前に必要なこと</li>
      <li>資金計画の基本を知る</li>
      <li>見積もりを正しく比べるコツ</li>
      <li>住宅会社選びに必要な視点</li>
      <li>自分の「住宅予算」に自信をもつ</li>
    </ul>
  </section>

  <div class="bottom"></div>
  <p class="office">もえぎうた事務局</p>
  <div class="tel">
    <svg width="46" height="46" viewBox="0 0 46 46" aria-hidden="true"><circle cx="23" cy="23" r="22" fill="#5e9b2a"/><path d="M15 13c2-1 4 0 5 2l1 3c0 1-1 2-2 3 1 3 3 5 6 6 1-1 2-2 3-2l3 1c2 1 3 3 2 5-1 2-3 3-5 2-8-2-13-7-15-15 0-2 0-4 2-5z" fill="#fff"/></svg>
    <span class="num">0120-555-018</span>
  </div>
  <p class="fax">FAX 06-6000-1234 <span>受付時間 平日 9:00〜17:00</span></p>
  <div class="web"><span class="tag">WEB予約</span><span class="url">https://moegiuta.or.jp</span></div>

  <section class="about">
    <h3>もえぎうたとは</h3>
    <p>もえぎうたは、家族が安心して暮らせる住まいづくりを応援する団体です。家づくりを考える方へ、中立の立場から正しい知識と判断基準をお届けし、後悔のない住まいづくりをサポートしています。</p>
  </section>
  <div class="search"><span class="q">もえぎうた</span><span class="btn">検索</span></div>
  <div class="footer-band"></div>
</main>
</body>
</html>
```